Business Card Design Project

QPR Management Consulting, LLC is a management consulting firm focused on improving an organization’s health and wellness while enhancing company performance with an emphasis on winning in the marketplace, profitable growth, team building, culture enablement and innovation.

Industry/Entity Type

Business

```html
<!DOCTYPE html>
<html lang="en">
<head>
<meta charset="utf-8">
<title>QPR Management Consulting – Business Card</title>
<link rel="stylesheet" href="https://fonts.googleapis.com/css2?family=Arimo:wght@400&family=Lato:wght@300&family=Tinos:wght@700&display=swap">
<style>
  :root {
    --page: #141414;
    --card: #2b2b2b;
    --ink: #f2f2f2;
    --muted: #bdbdbd;
    --green: #7cc242;
  }
  * { margin: 0; padding: 0; box-sizing: border-box; }
  html, body { width: 960px; height: 1200px; overflow: hidden; background: var(--page); }
  body { position: relative; font-family: "Arimo", Arial, sans-serif; color: var(--ink); }

  .card {
    position: absolute;
    left: 80px;
    width: 800px;
    height: 457px;
    background: var(--card);
    box-shadow: 0 8px 30px rgba(0,0,0,.5);
  }
  .card--front { top: 110px; }
  .card--back  { top: 630px; }

  .brand { position: absolute; font-family: "Lato", sans-serif; font-weight: 300; color: var(--muted); line-height: 1; }
  .brand__name { display: block; }
  .brand__sub { display: block; }

  .card--front .brand { left: 56px; top: 62px; }
  .card--front .brand__name { font-size: 64px; }
  .card--front .brand__sub { font-size: 25px; margin-top: 4px; }

  .card--back .brand { left: 440px; top: 44px; }
  .card--back .brand__name { font-size: 54px; }
  .card--back .brand__sub { font-size: 21px; margin-top: 2px; }

  .person { position: absolute; left: 52px; top: 254px; }
  .person__name { font-family: "Tinos", serif; font-weight: 700; font-size: 27px; line-height: 1; letter-spacing: .5px; }
  .person__role { font-size: 19px; color: var(--green); margin-top: 1px; }

  .divider { position: absolute; left: 52px; top: 322px; width: 704px; height: 2px; background: var(--green); opacity: .8; }

  .contact { position: absolute; left: 52px; top: 340px; list-style: none; font-size: 19px; line-height: 25px; }
  .contact li { display: flex; align-items: center; gap: 10px; }
  .contact svg { width: 16px; height: 16px; fill: var(--green); }

  .address { position: absolute; right: 36px; top: 368px; text-align: right; font-size: 19px; line-height: 25px; }

  .offerings { position: absolute; left: 43px; top: 40px; }
  .offerings__title { font-size: 19px; color: var(--green); text-transform: uppercase; margin-bottom: 18px; }
  .offerings__list { list-style: none; font-size: 19px; line-height: 24.6px; }
  .offerings__list li { position: relative; padding-left: 29px; }
  .offerings__list li::before {
    content: ""; position: absolute; left: 3px; top: 9px; width: 8px; height: 8px; border-radius: 50%; background: var(--green);
  }

  .subservices { position: absolute; top: 345px; list-style: none; font-size: 19px; line-height: 24.6px; }
  .subservices li { display: flex; }
  .subservices .num { color: var(--green); min-width: 22px; }
  .subservices--a { left: 43px; }
  .subservices--b { left: 512px; }
</style>
</head>
<body>

<section class="card card--front" aria-label="Card front">
  <div class="brand">
    <span class="brand__name">QPR</span>
    <span class="brand__sub">Management Consulting, LLC</span>
  </div>

  <div class="person">
    <p class="person__name">DANIEL REEVE</p>
    <p class="person__role">Managing Director</p>
  </div>

  <div class="divider"></div>

  <ul class="contact">
    <li>
      <svg viewBox="0 0 16 16" aria-hidden="true"><path d="M4 0h8a1 1 0 0 1 1 1v14a1 1 0 0 1-1 1H4a1 1 0 0 1-1-1V1a1 1 0 0 1 1-1zm.5 2v10h7V2zM8 13a1 1 0 1 0 0 2 1 1 0 0 0 0-2z"/></svg>
      (03) 5550 1842
    </li>
    <li>
      <svg viewBox="0 0 16 16" aria-hidden="true"><path d="M4 0h8v4H4zM1 5h14a1 1 0 0 1 1 1v6h-3v4H3v-4H0V6a1 1 0 0 1 1-1zm3 6v4h8v-4z"/></svg>
      (03) 5550 1842
    </li>
    <li>
      <svg viewBox="0 0 16 16" aria-hidden="true"><path d="M0 3h16v1L8 9 0 4zM0 5.5l8 5 8-5V13H0z"/></svg>
      info@qprconsulting.com
    </li>
  </ul>

  <address class="address" style="font-style:normal">
    PO BOX&nbsp; 418 Harlow Lane<br>Kensington Melbourne
  </address>
</section>

<section class="card card--back" aria-label="Card back">
  <div class="offerings">
    <h2 class="offerings__title" style="font-weight:400">Service Offerings</h2>
    <ul class="offerings__list">
      <li>Organizational Health Services</li>
      <li>Company Turnaround Services</li>
      <li>Innovation Lab Establishment</li>
      <li>Enterprise Risk Management</li>
      <li>Business Strategy Development</li>
      <li>Strategic Corporate Communication Strategy Development</li>
      <li>IT Strategy Development</li>
      <li>Complex Program and Project Management</li>
      <li>M&amp;A due diligence support</li>
      <li>Post-M&amp;A Integration Services including:</li>
    </ul>
  </div>

  <div class="brand">
    <span class="brand__name">QPR</span>
    <span class="brand__sub">Management Consulting, LLC</span>
  </div>

  <ol class="subservices subservices--a">
    <li><span class="num">1.</span>Change Management</li>
    <li><span class="num">2.</span>Organization Design</li>
    <li><span class="num">3.</span>Integrated Business Strategy Development</li>
  </ol>
  <ol class="subservices subservices--b">
    <li><span class="num">4.</span>IT Integration Strategy</li>
    <li><span class="num"></span>Development</li>
    <li><span class="num">5.</span>Leadership Development</li>
  </ol>
</section>

</body>
</html>
```